Clean and modern business cards

Looking for an updated business card design for my dental office “corvanta dental” . Looking for a modern clean / sleek design . I’m thinking black background but open to seeing other options . One side needs to have an appointment card . Card needs to have logo, dentist name , phone, email , address . I’ve attached couple of cards I thought were cool as well as my logo
Target Market(s)
Dental patients
Industry/Entity Type
Dentistry
Contact Information for Business Card
Phone email address

```html
<!DOCTYPE html>
<html lang="en">
<head>
<meta charset="utf-8">
<title>Corvanta Dental – Business Card</title>
<link href="https://fonts.googleapis.com/css2?family=Poppins:wght@400;500;600;700&display=swap" rel="stylesheet">
<style>
  :root {
    --stage: #3a3736;
    --card-dark: #050505;
    --card-light: #ffffff;
    --ink-light: #ffffff;
    --ink-dark: #111111;
    --accent: #2aa7c0;
    --rule: #1a1a1a;
  }
  * { box-sizing: border-box; margin: 0; padding: 0; }
  html, body { width: 1200px; height: 1200px; overflow: hidden; }
  body {
    background: var(--stage);
    font-family: "Poppins", sans-serif;
    position: relative;
  }
  .card {
    position: absolute;
    left: 220px;
    width: 760px;
    height: 432px;
    overflow: hidden;
  }
  /* Front */
  .card-front { top: 140px; background: var(--card-dark); color: var(--ink-light); }
  .front-decor {
    position: absolute; left: 440px; top: 40px; width: 380px; height: 380px; border-radius: 50%;
    background: radial-gradient(circle, rgba(255,255,255,0.07) 0%, rgba(255,255,255,0.03) 55%, rgba(255,255,255,0) 72%);
  }
  .front-brand {
    position: absolute; left: 120px; top: 118px; display: flex; align-items: center; gap: 30px;
  }
  .brand-dot { width: 150px; height: 150px; border-radius: 50%; background: var(--accent); flex: none; }
  .brand-name {
    font-weight: 600; color: var(--ink-light); line-height: 1.05; text-transform: uppercase;
  }
  .front-brand .brand-name { font-size: 52px; letter-spacing: 1px; }
  .brand-name .sub { display: block; font-size: 0.52em; letter-spacing: 0.42em; text-align: right; }
  .front-contact {
    position: absolute; left: 0; width: 760px; top: 318px; padding-right: 10px;
    text-align: center; font-size: 15px; letter-spacing: 1.6px; font-weight: 400; line-height: 33px;
  }
  .front-contact p { text-transform: uppercase; }

  /* Back */
  .card-back { top: 628px; background: var(--card-light); color: var(--ink-dark); }
  .back-decor {
    position: absolute; right: -60px; top: -10px; width: 360px; height: 460px; border-radius: 50%;
    background: radial-gradient(ellipse, rgba(170,200,230,0.35) 0%, rgba(240,210,150,0.2) 45%, rgba(255,255,255,0) 72%);
  }
  .back-info { position: absolute; left: 0; top: 50px; width: 300px; text-align: center; }
  .back-brand { display: flex; align-items: center; justify-content: center; gap: 12px; margin-bottom: 36px; }
  .back-brand .brand-dot { width: 62px; height: 62px; }
  .back-brand .brand-name { color: var(--ink-dark); font-size: 24px; }
  .back-info p { font-size: 15px; font-weight: 600; letter-spacing: 0.5px; text-transform: uppercase; line-height: 19px; }
  .back-info .phone { margin-top: 26px; }
  .back-info .web { margin-top: 26px; letter-spacing: 2px; }
  .divider { position: absolute; left: 300px; top: 22px; width: 2px; height: 372px; background: var(--rule); }
  .appointment { position: absolute; left: 310px; width: 450px; top: 30px; text-align: center; }
  .appointment h2 { font-size: 17px; font-weight: 500; letter-spacing: 3px; text-transform: uppercase; }
  .field { margin: 36px auto 0; width: 350px; border-top: 1.5px solid var(--ink-dark); padding-top: 4px;
    font-size: 15px; letter-spacing: 1.5px; text-transform: uppercase; }
  .field + .field { margin-top: 58px; }
  .notice { margin-top: 42px; font-size: 15px; font-weight: 500; line-height: 19px; padding: 0 20px; }
  .email { margin-top: 18px; font-size: 15px; font-weight: 600; letter-spacing: 1.5px; text-transform: uppercase; }
</style>
</head>
<body>
  <section class="card card-front" aria-label="Card front">
    <div class="front-decor" role="img" aria-label="Faint circular brand pattern"></div>
    <div class="front-brand">
      <span class="brand-dot"></span>
      <h1 class="brand-name">Corvanta<span class="sub">Dental</span></h1>
    </div>
    <div class="front-contact">
      <p>482 Larkfield Ave, Brandon, MB</p>
      <p>corvantadental.ca</p>
    </div>
  </section>

  <section class="card card-back" aria-label="Appointment card">
    <div class="back-decor" role="img" aria-label="Faint colourful brand pattern"></div>
    <div class="back-info">
      <div class="back-brand">
        <span class="brand-dot"></span>
        <span class="brand-name">Corvanta<span class="sub">Dental</span></span>
      </div>
      <p>482 Larkfield Ave,<br>Brandon, MB</p>
      <p class="phone">(204) 555-0192</p>
      <p class="web">corvantadental.ca</p>
    </div>
    <div class="divider"></div>
    <div class="appointment">
      <h2>Your next appointment is:</h2>
      <div class="field">Date</div>
      <div class="field">Time</div>
      <p class="notice">To cancel or reschedule please notify us at least 48 hours prior to your scheduled appointment</p>
      <p class="email">contact@corvantadental.ca</p>
    </div>
  </section>
</body>
</html>
```